Young Makers Competition Event For Teenagers Needs Promo Graphics

I am in need of graphics for 2019 Northmere Young Makers Festival. It is a Young Makers competition event for teenagers. I need graphics to make an 11x17 poster and a main title graphic that I can use for digital (social, 16x9 for screens, etc). Graphic should include the following 2 logos: the QW Brightpath logo (this is who we are) and the "circles" logo is the logo of Young Makers Festival so that can be incorporated but is not mandatory and does not need to be in color. Tag line for Young Makers is "Discover. Develop. Deploy." Again, this is optional. Looking for an artistic design - geometric shapes, bright colors, or something along those lines. Something that speaks to teenagers and especially creatives/Young Makers types. Additionally, Post should include:
Maple Ridge Chapel
March 29-30
(registration & cost info may be added to the poster before design is finalized; still working on those details)

```html
<!DOCTYPE html>
<html lang="en">
<head>
<meta charset="utf-8">
<title>Northmere Young Makers Festival</title>
<link rel="stylesheet" href="https://fonts.googleapis.com/css2?family=Baloo+2:wght@700;800&family=Nunito:wght@800;900&display=swap">
<style>
  :root {
    --paper: #ffffff;
    --cream: #fbf6df;
    --sun: #f6cd5c;
    --sky: #8ed0dc;
    --sky-soft: #c9e8ef;
    --navy: #25378b;
    --blue: #3f63b0;
    --rose: #e23b63;
    --rose-soft: #f4b6c6;
    --ember: #e0572b;
    --gold-line: #f3c24a;
  }
  html, body {
    margin: 0;
    padding: 0;
    overflow: hidden;
    background: var(--paper);
  }
  .poster {
    position: relative;
    width: 873px;
    height: 1200px;
    overflow: hidden;
    background: var(--paper);
  }
  .poster-art {
    display: block;
    width: 873px;
    height: 1200px;
  }
  .title-type {
    font-family: "Baloo 2", "Arial Rounded MT Bold", sans-serif;
    font-weight: 800;
  }
  .detail-type {
    font-family: "Nunito", "Helvetica Neue", sans-serif;
    font-weight: 900;
  }
  .kicker { fill: var(--sun); }
  .word-young { fill: var(--sky); }
  .word-makers { fill: var(--navy); }
  .word-festival { fill: var(--rose); }
  .event-date { fill: var(--navy); }
  .event-venue { fill: var(--navy); font-weight: 800; }
  .brand-name { fill: var(--navy); }
  .festival-mark-name { fill: var(--navy); }
  .band { fill: var(--cream); }
  .gold-rule { stroke: var(--gold-line); stroke-width: 1.6; stroke-linecap: round; }
  .ember-tick { stroke: var(--ember); stroke-width: 3; }
  .pale-stripe { stroke: var(--sky); stroke-width: 3; }
</style>
</head>
<body>
<main class="poster">
  <svg class="poster-art" viewBox="0 0 573 788" xmlns="http://www.w3.org/2000/svg" aria-labelledby="poster-title">
    <title id="poster-title">Northmere Young Makers Festival, 29-30 March, Maple Ridge Chapel</title>
    <defs>
      <linearGradient id="grad-sky" x1="0" y1="0" x2="1" y2="1">
        <stop offset="0" stop-color="#d6eef3"/>
        <stop offset="1" stop-color="#6fb7d2"/>
      </linearGradient>
      <linearGradient id="grad-blue" x1="0" y1="0" x2="1" y2="1">
        <stop offset="0" stop-color="#2f4f9e"/>
        <stop offset="1" stop-color="#8cc7e0"/>
      </linearGradient>
      <linearGradient id="grad-glass" x1="0" y1="0" x2="1" y2="0">
        <stop offset="0" stop-color="#e7f5f8"/>
        <stop offset="1" stop-color="#9fd4e2"/>
      </linearGradient>
      <linearGradient id="grad-navy" x1="0" y1="0" x2="1" y2="1">
        <stop offset="0" stop-color="#25378b"/>
        <stop offset="1" stop-color="#3c5cab"/>
      </linearGradient>
    </defs>

    <!-- background bands -->
    <g class="bands">
      <polygon class="band" points="60,650 540,175 540,268 60,742"/>
      <polygon class="band" points="130,788 555,340 555,440 230,788"/>
    </g>

    <!-- thin gold rules -->
    <g class="gold-rules">
      <line class="gold-rule" x1="300" y1="300" x2="352" y2="262"/>
      <line class="gold-rule" x1="240" y1="410" x2="345" y2="318"/>
      <line class="gold-rule" x1="445" y1="345" x2="540" y2="262"/>
      <line class="gold-rule" x1="110" y1="610" x2="170" y2="556"/>
      <line class="gold-rule" x1="370" y1="545" x2="450" y2="470"/>
      <line class="gold-rule" x1="40" y1="760" x2="130" y2="675"/>
      <line class="gold-rule" x1="225" y1="495" x2="245" y2="478"/>
      <line class="gold-rule" x1="460" y1="610" x2="530" y2="548"/>
    </g>

    <!-- corner and accent shapes -->
    <polygon class="shape-corner" points="30,28 124,28 30,112" fill="url(#grad-sky)" role="img" aria-label="Blue triangle with fine wave texture"/>
    <polygon class="shape-glass" points="442,262 505,230 505,300 442,330" fill="url(#grad-glass)"/>
    <polygon class="shape-tri-navy" points="415,372 480,305 480,372" fill="url(#grad-blue)"/>
    <polygon class="shape-glass" points="460,470 525,438 525,500 460,532" fill="url(#grad-glass)"/>
    <polygon class="shape-tri-low" points="483,607 548,607 483,672" fill="url(#grad-blue)"/>
    <polygon class="shape-corner-low" points="128,722 180,650 180,722" fill="url(#grad-sky)" role="img" aria-label="Blue triangle with fine wave texture"/>

    <!-- orange ticks -->
    <g class="ember-ticks">
      <line class="ember-tick" x1="291" y1="408" x2="291" y2="444"/>
      <line class="ember-tick" x1="300" y1="398" x2="300" y2="436"/>
      <line class="ember-tick" x1="309" y1="388" x2="309" y2="428"/>
      <line class="ember-tick" x1="318" y1="378" x2="318" y2="420"/>
      <line class="ember-tick" x1="327" y1="368" x2="327" y2="412"/>
      <line class="ember-tick" x1="336" y1="358" x2="336" y2="404"/>
    </g>

    <!-- dotted triangle -->
    <polygon class="shape-dots" points="355,380 470,380 355,522" fill="var(--rose-soft)" opacity="0.55" role="img" aria-label="Pink dot grid triangle"/>

    <!-- hexagon tile -->
    <rect class="tile-hex" x="193" y="457" width="144" height="143" fill="url(#grad-sky)" role="img" aria-label="Light blue square with hexagon pattern"/>

    <!-- pale vertical stripes -->
    <g class="pale-stripes">
      <line class="pale-stripe" x1="204" y1="640" x2="204" y2="720"/>
      <line class="pale-stripe" x1="214" y1="630" x2="214" y2="720"/>
      <line class="pale-stripe" x1="224" y1="620" x2="224" y2="720"/>
      <line class="pale-stripe" x1="234" y1="610" x2="234" y2="720"/>
      <line class="pale-stripe" x1="244" y1="600" x2="244" y2="720"/>
      <line class="pale-stripe" x1="254" y1="590" x2="254" y2="710"/>
      <line class="pale-stripe" x1="264" y1="580" x2="264" y2="700"/>
      <line class="pale-stripe" x1="274" y1="570" x2="274" y2="690"/>
      <line class="pale-stripe" x1="284" y1="560" x2="284" y2="680"/>
      <line class="pale-stripe" x1="294" y1="550" x2="294" y2="670"/>
      <line class="pale-stripe" x1="304" y1="540" x2="304" y2="660"/>
      <line class="pale-stripe" x1="314" y1="530" x2="314" y2="650"/>
      <line class="pale-stripe" x1="324" y1="520" x2="324" y2="640"/>
      <line class="pale-stripe" x1="334" y1="510" x2="334" y2="630"/>
      <line class="pale-stripe" x1="474" y1="572" x2="474" y2="592"/>
      <line class="pale-stripe" x1="482" y1="566" x2="482" y2="588"/>
      <line class="pale-stripe" x1="490" y1="560" x2="490" y2="584"/>
      <line class="pale-stripe" x1="498" y1="554" x2="498" y2="580"/>
    </g>

    <!-- navy weave tile -->
    <rect class="tile-weave" x="236" y="540" width="214" height="176" fill="url(#grad-navy)" role="img" aria-label="Navy square with basket weave pattern"/>

    <!-- title -->
    <text class="title-type kicker" font-size="32" textLength="185" lengthAdjust="spacingAndGlyphs" transform="translate(40,192) rotate(-44)">NORTHMERE</text>
    <text class="title-type" font-size="64" textLength="433" lengthAdjust="spacingAndGlyphs" transform="translate(24,346) rotate(-44)"><tspan class="word-young">YOUNG</tspan> <tspan class="word-makers">MAKERS</tspan></text>
    <text class="title-type word-festival" font-size="78" textLength="385" lengthAdjust="spacingAndGlyphs" transform="translate(182,332) rotate(-44)">FESTIVAL</text>

    <!-- event details -->
    <text class="detail-type event-date" font-size="38" textLength="230" lengthAdjust="spacingAndGlyphs" transform="translate(362,268) rotate(-44)">29-30 MART</text>
    <text class="detail-type event-venue" font-size="21" textLength="208" lengthAdjust="spacingAndGlyphs" transform="translate(394,284) rotate(-44)">Maple Ridge Chapel</text>

    <!-- host brand -->
    <g class="host-brand">
      <circle cx="44" cy="518" r="16" fill="var(--sky)"/>
      <text class="title-type brand-name" x="66" y="514" font-size="21">QW</text>
      <text class="title-type brand-name" x="66" y="536" font-size="21">Brightpath</text>
    </g>

    <!-- festival mark -->
    <g class="festival-mark">
      <circle cx="515" cy="712" r="12" fill="var(--sky)"/>
      <text class="title-type festival-mark-name" x="515" y="742" font-size="11" text-anchor="middle">Young Makers</text>
      <text class="title-type festival-mark-name" x="515" y="755" font-size="11" text-anchor="middle">Festival</text>
    </g>
  </svg>
</main>
</body>
</html>
```